Events floral designer business needs a logo design

I need a logo design for my floral design business called tender thorns.
i am inspired by nature and the simplicity of its beauty, whilst upcycling and recycling materials to reduce waste and impact on our environment.
I would like the design to be printed on recycled brown cardboard so i would like a simple but striking design of a bold black ivy vine or gnarly magnolia or tree branch with lower case old school type writer font.

Target Market(s)

Anyone requiring floral additions for their event

Industry/Entity Type

Business

Contact Information for Business Card

mara hollis
floral designer/creator
0418657203
mara@tenderthorns.com
tenderthorns.com

Font styles to use
Other font styles liked:
• lower case type writer

Colors
000000

Requirements
Must have
• simplicity but boldness
• Black typewriter font and bold picture with my details
Nice to have
• as above
Should not have
• colour

```html
<!DOCTYPE html>
<html lang="en">
<head>
<meta charset="utf-8">
<title>Tender Thorns – Mara Hollis</title>
<link href="https://fonts.googleapis.com/css2?family=Questrial&display=swap" rel="stylesheet">
<style>
  :root {
    --backdrop: #000000;
    --kraft: #d6c8b3;
    --kraft-light: #ddd1bf;
    --kraft-fleck-dark: rgba(120, 95, 70, 0.22);
    --kraft-fleck-light: rgba(245, 238, 226, 0.55);
    --watermark: rgba(236, 226, 210, 0.75);
    --ink: #121110;
  }
  html, body {
    margin: 0;
    padding: 0;
    width: 1189px;
    height: 1200px;
    overflow: hidden;
    background: var(--backdrop);
  }
  .canvas {
    position: relative;
    width: 1189px;
    height: 1200px;
  }
  .business-card {
    position: absolute;
    left: 295px;
    top: 74px;
    width: 600px;
    height: 1052px;
    border-radius: 26px;
    overflow: hidden;
    background-color: var(--kraft);
    background-image:
      radial-gradient(circle, var(--kraft-fleck-dark) 0 1px, transparent 1.6px),
      radial-gradient(circle, var(--kraft-fleck-light) 0 1px, transparent 1.6px),
      radial-gradient(circle, var(--kraft-fleck-dark) 0 0.8px, transparent 1.3px),
      radial-gradient(ellipse at 45% 30%, var(--kraft-light), var(--kraft));
    background-size: 37px 41px, 29px 23px, 17px 19px, 100% 100%;
    background-position: 3px 7px, 11px 2px, 5px 13px, 0 0;
    font-family: "Questrial", "Century Gothic", sans-serif;
    color: var(--ink);
    text-align: center;
  }
  .watermark-flourish {
    position: absolute;
    left: -40px;
    top: 520px;
    width: 440px;
    height: 540px;
    background: radial-gradient(ellipse at 40% 45%, var(--watermark), transparent 70%);
  }
  .brand-mark {
    position: absolute;
    left: 0;
    top: 72px;
    width: 100%;
  }
  .brand-mark__name {
    margin: 0;
    font-size: 54px;
    font-weight: 400;
    letter-spacing: 9px;
    line-height: 1;
  }
  .brand-mark__circle {
    display: block;
    margin: 26px auto 0;
    position: relative;
    left: 20px;
  }
  .person {
    position: absolute;
    left: 0;
    top: 566px;
    width: 100%;
  }
  .person__name {
    margin: 0;
    font-size: 60px;
    font-weight: 400;
    line-height: 1.1;
  }
  .person__role {
    margin: 4px 0 0;
    font-size: 40px;
    line-height: 1.2;
  }
  .contact {
    position: absolute;
    left: 0;
    top: 762px;
    width: 100%;
    margin: 0;
    padding: 0;
    list-style: none;
    font-size: 42px;
    line-height: 50px;
    letter-spacing: 0.5px;
  }
  .contact__label {
    font-weight: 400;
    -webkit-text-stroke: 0.6px var(--ink);
  }
</style>
</head>
<body>
<main class="canvas">
  <article class="business-card">
    <div class="watermark-flourish" role="img" aria-label="Faint vine flourish watermark behind the contact details"></div>

    <header class="brand-mark">
      <p class="brand-mark__name">tender thorns</p>
      <svg class="brand-mark__circle" width="320" height="320" viewBox="0 0 320 320" aria-hidden="true">
        <circle cx="160" cy="160" r="153" fill="none" stroke="#121110" stroke-width="7"/>
      </svg>
    </header>

    <section class="person">
      <h1 class="person__name">Mara Hollis</h1>
      <p class="person__role">Floral designer/creator</p>
    </section>

    <ul class="contact">
      <li><span class="contact__label">p:</span> 0418657203</li>
      <li><span class="contact__label">e:</span> mara@tenderthorns.com</li>
      <li><span class="contact__label">w:</span> tenderthorns.com</li>
    </ul>
  </article>
</main>
</body>
</html>
```